BOOK COVER for THE IRONCLAD FOUNDER

I am publishing my first book and need to nail the cover. The cover should feature my picture as this is a major branding play.
TITLE: The Ironclad Founder.
SUBTITLE: Crafting A Steadfast Company Heritage.
BOOK DESCRIPTION: "The Ironclad Founder," presents a comprehensive approach to building resilient and sustainable businesses. The book emphasizes the inevitability of challenges in the business world and stresses the importance of resilience in facing adversity. It highlights the concept of "Shatterproofing" a business, drawing inspiration from the safety glass used in car windshields, which doesn't shatter upon impact​​.

The book identifies two primary types of business owners: "CAPTIVES," who are overwhelmed and cannot take a break from their businesses without facing chaos, and "SHATTERPROOF" entrepreneurs, who have established systems and processes, clear goals, and can step away from their businesses without encountering problems​​. It raises critical questions about why some business owners become "CAPTIVES" while others achieve a "SHATTERPROOF" state and explores the transition from one to the other​​.

Dunmore points out that many well-intentioned business founders often lack a comprehensive roadmap or blueprint, leading to vulnerabilities in their businesses​​. Reflecting on his own journey from being a "CAPTIVE" to becoming "SHATTERPROOF," Dunmore shares insights from his experiences and the lessons he learned along the way​​.

The book addresses the legal aspects of businesses, an often overlooked area in entrepreneurial literature, providing readers with a roadmap and the necessary legal systems and structures to build a "SHATTERPROOF" business​​. This approach led to the development of Dunmore's Keystone Counsel Mentoring Plan and the Ironclad Method​​.

Dunmore encourages business owners to shift their paradigm, viewing lawyers as primary care providers for their businesses rather than turning to them only in emergencies​​. "The Ironclad Founder" is an invitation to make this paradigm shift and provides a roadmap for becoming a resilient and successful entrepreneur​​.

Target Market(s)

Small business owners from Start-up to $10 Million

Industry/Entity Type

Legal / Entrepreneurship

Font styles to use
Serif

Colors
0054AA
0677BA
7BADD7
CADEEF
E8F1F8

Requirements
Must have
• I am publishing my first book and need to nail the cover. The cover should feature my picture as this is a major branding play. The foreward has been written by Paul Vantrees. This needs to be included in the cover.

```html
<!DOCTYPE html>
<html lang="en">
<head>
<meta charset="UTF-8">
<title>The Ironclad Founder — Book Cover</title>
<link href="https://fonts.googleapis.com/css2?family=Bebas+Neue&family=Montserrat:wght@400;500&family=Arimo&display=swap" rel="stylesheet">
<style>
  :root {
    --page: #ffffff;
    --navy-deep: #020c3a;
    --navy: #0a1f8c;
    --ink: #000000;
    --accent: #4a80e8;
    --white: #ffffff;
    --subtle: #e6e9f2;
    --suit-light: #2d4f92;
    --suit-dark: #17305f;
  }
  * { margin: 0; padding: 0; box-sizing: border-box; }
  html, body {
    width: 727px;
    height: 1200px;
    overflow: hidden;
    background: var(--page);
  }
  .canvas {
    position: relative;
    width: 727px;
    height: 1200px;
  }
  .cover {
    position: absolute;
    left: 64px;
    top: 55px;
    width: 589px;
    height: 883px;
    overflow: hidden;
    background:
      linear-gradient(90deg, var(--navy) 0%, var(--navy-deep) 38%, #010414 62%, var(--ink) 72%);
  }
  .portrait {
    position: absolute;
    left: 0;
    top: 45px;
    width: 440px;
    height: 838px;
    border-radius: 46% 46% 0 0 / 22% 22% 0 0;
    background: linear-gradient(160deg, var(--suit-light) 0%, #24437f 45%, var(--suit-dark) 100%);
  }
  .author {
    position: absolute;
    right: 40px;
    top: 112px;
    text-align: right;
    font-family: 'Montserrat', sans-serif;
    font-weight: 400;
    font-size: 40px;
    line-height: 46px;
    letter-spacing: 1px;
    color: var(--accent);
  }
  .author-line { display: block; }
  .title {
    position: absolute;
    left: 31px;
    top: 468px;
    font-family: 'Bebas Neue', sans-serif;
    font-weight: 400;
    font-size: 100px;
    line-height: 97px;
    color: var(--white);
  }
  .title-line { display: block; }
  .title-accent { color: var(--accent); }
  .subtitle {
    position: absolute;
    left: 0;
    width: 100%;
    top: 760px;
    text-align: center;
    font-family: 'Bebas Neue', sans-serif;
    font-size: 34px;
    line-height: 1;
    color: var(--white);
  }
  .foreword {
    position: absolute;
    left: 0;
    width: 100%;
    top: 822px;
    text-align: center;
    font-family: 'Montserrat', sans-serif;
    font-weight: 500;
    font-size: 17px;
    letter-spacing: 3.5px;
    color: var(--subtle);
  }
  .draft-note {
    position: absolute;
    left: 273px;
    top: 1006px;
    width: 454px;
    height: 109px;
    background: var(--ink);
    color: var(--white);
    font-family: 'Arimo', Arial, sans-serif;
    font-size: 24px;
    line-height: 28px;
    padding: 13px 0 0 23px;
  }
</style>
</head>
<body>
<div class="canvas">
  <section class="cover">
    <div class="portrait" role="img" aria-label="Author portrait: bearded man in glasses and a navy suit, arms crossed"></div>
    <p class="author">
      <span class="author-line">GRANT</span>
      <span class="author-line">DUNMORE</span>
    </p>
    <h1 class="title">
      <span class="title-line">THE</span>
      <span class="title-line title-accent">IRONCLAD</span>
      <span class="title-line">FOUNDER</span>
    </h1>
    <p class="subtitle">CRAFTING A STEADFAST COMPANY HERITAGE</p>
    <p class="foreword">FOREWORD BY PAUL VANTREES</p>
  </section>
  <aside class="draft-note">
    New Draft:<br>
    New version for proof of concept<br>
    for the next round of feedback
  </aside>
</div>
</body>
</html>
```